Love pets? Create a veterinary business card that aligns with our new revamped website.

Greetings! We are a five-doctor veterinary hospital that seeks your expertise in designing a new business card that harmonizes with our recently revitalized website: www.tqrn.net. The card should feature our logo, the five doctors, operating hours, contact information, and communicate our purpose and personality.

Contact Information for Business Card

TBA

```html
<!DOCTYPE html>
<html lang="en">
<head>
<meta charset="utf-8">
<title>Tranquil Ridge Veterinary Hospital – Business Card</title>
<link rel="stylesheet" href="https://fonts.googleapis.com/css2?family=Arimo:wght@400;700&display=swap">
<style>
  :root {
    --backdrop: #2b2c2e;
    --card: #f4f4f4;
    --green: #3f8a3a;
    --brown: #9a6a2a;
    --ink: #222222;
    --rule: #c9c9c9;
  }
  * { margin: 0; padding: 0; box-sizing: border-box; }
  html, body { width: 1200px; height: 912px; overflow: hidden; }
  body {
    background: var(--backdrop);
    font-family: "Arimo", Arial, sans-serif;
    position: relative;
  }
  .card {
    position: absolute;
    width: 560px;
    height: 320px;
    background: var(--card);
    border-radius: 22px;
    box-shadow: 0 10px 30px rgba(0,0,0,.45);
  }
  .card--front { left: 70px; top: 100px; }
  .card--back { left: 570px; top: 490px; }

  /* front */
  .front-brand {
    position: absolute;
    left: 0; right: 0; top: 120px;
    display: flex; align-items: center; justify-content: center; gap: 12px;
  }
  .brand-dot { width: 16px; height: 16px; border-radius: 50%; background: var(--green); }
  .front-brand .brand-name {
    color: var(--green); font-size: 30px; font-weight: 700;
  }
  .front-web {
    position: absolute; left: 0; right: 0; top: 226px;
    text-align: center; font-size: 15px; letter-spacing: 5px; color: var(--ink);
  }

  /* back */
  .back-brand {
    position: absolute; left: 34px; top: 152px; width: 230px;
    color: var(--green); font-size: 19px; font-weight: 700; line-height: 1.25;
  }
  .divider {
    position: absolute; left: 292px; top: 36px; width: 1px; height: 248px;
    background: var(--rule);
  }
  .contact { position: absolute; left: 318px; top: 60px; color: var(--ink); }
  .contact__name { color: var(--green); font-size: 24px; font-weight: 700; }
  .contact__role { color: var(--brown); font-size: 16px; margin-top: 2px; }
  .contact__address { font-size: 15px; line-height: 1.3; margin-top: 14px; }
  .contact__list { list-style: none; margin-top: 12px; font-size: 15px; line-height: 1.45; }
  .contact__list li { display: flex; align-items: center; gap: 8px; }
  .contact__list svg { width: 13px; height: 13px; fill: var(--green); flex: none; }
</style>
</head>
<body>
  <section class="card card--front" aria-label="Card front">
    <div class="front-brand">
      <span class="brand-dot"></span>
      <span class="brand-name">Tranquil Ridge</span>
    </div>
    <p class="front-web">www.tqrn.net</p>
  </section>

  <section class="card card--back" aria-label="Card back">
    <p class="back-brand">Tranquil Ridge Veterinary Hospital</p>
    <div class="divider"></div>
    <div class="contact">
      <p class="contact__name">Owen Hartley</p>
      <p class="contact__role">President</p>
      <p class="contact__address">4820 Cedar Hollow Road,<br>Denton, TX 76201</p>
      <ul class="contact__list">
        <li>
          <svg viewBox="0 0 24 24"><path d="M6.6 10.8a15.1 15.1 0 0 0 6.6 6.6l2.2-2.2c.3-.3.7-.4 1-.2 1.1.4 2.3.6 3.6.6.6 0 1 .4 1 1V20c0 .6-.4 1-1 1A17 17 0 0 1 3 4c0-.6.4-1 1-1h3.5c.6 0 1 .4 1 1 0 1.3.2 2.5.6 3.6.1.3 0 .7-.2 1z"/></svg>
          (940) 555-0182
        </li>
        <li>
          <svg viewBox="0 0 24 24"><path d="M2 5h20v14H2z M2 5l10 8 10-8" fill="none" stroke="#3f8a3a" stroke-width="2.4"/></svg>
          info@tqrn.net
        </li>
        <li>
          <svg viewBox="0 0 24 24"><circle cx="12" cy="12" r="10"/></svg>
          www.tqrn.net
        </li>
      </ul>
    </div>
  </section>
</body>
</html>
```